New hardcover book cover

I want a striking, eye-catching cover with title, subtitle and a picture.See for previous book covers: www.brightmaplepress.com

Target Market(s)

young, successful entrepreneurs that have built a business in a niche market that they discovered.

Font styles to use
Serif

Colors

Designer to choose colors to be used in the design.

Requirements
Must have
• A book cover that impresses and captures the imagination of those who look at it.
• MY MISTAKE, SORRY.
• Title: Founders Behind the Quiet Trade Boom
• Subtitle: 25 stories of success from
• discovering hidden opportunities
• Author: Dorian Pelham
• Please use the photo attached, thanks.

```html
<!DOCTYPE html>
<html lang="en">
<head>
<meta charset="utf-8">
<title>Founders Behind the Quiet Trade Boom — Book Cover</title>
<link rel="stylesheet" href="https://fonts.googleapis.com/css2?family=Roboto+Slab:wght@200;300&display=swap">
<style>
  :root {
    --backdrop: #a5a6aa;
    --paper: #ffffff;
    --paper-shade: #e4e5e7;
    --ink: #24242c;
    --rule: #3a3a42;
    --gem-light: #a9d4ef;
    --gem-mid: #6fa7cc;
    --rock-mid: #3b434d;
    --rock-dark: #1c2128;
  }
  * { box-sizing: border-box; margin: 0; padding: 0; }
  html, body {
    width: 1200px;
    height: 1000px;
    overflow: hidden;
    background: var(--backdrop);
  }
  .canvas {
    position: relative;
    width: 1200px;
    height: 1000px;
  }
  .book-cover {
    position: absolute;
    left: 300px;
    top: 58px;
    width: 617px;
    height: 862px;
    background: var(--paper);
    color: var(--ink);
    font-family: "Roboto Slab", "Rockwell", serif;
    font-weight: 300;
    border-radius: 2px 4px 4px 2px;
    box-shadow: 0 12px 30px rgba(0, 0, 0, 0.22), 0 2px 6px rgba(0, 0, 0, 0.12);
  }
  .cover-spine {
    position: absolute;
    left: 0;
    top: 0;
    width: 42px;
    height: 100%;
    background: linear-gradient(90deg, var(--paper-shade) 0%, var(--paper) 30%, var(--paper) 72%, var(--paper-shade) 88%, var(--paper) 100%);
  }
  .title-line {
    position: absolute;
    left: 0;
    width: 100%;
    text-align: center;
    padding-left: 34px;
    white-space: nowrap;
    font-weight: 300;
  }
  .title-lead { top: 66px; font-size: 55px; line-height: 60px; }
  .title-join { top: 118px; font-size: 17px; line-height: 20px; padding-left: 0; left: -40px; }
  .title-main-1 { top: 128px; font-size: 76px; line-height: 80px; }
  .title-main-2 { top: 200px; font-size: 76px; line-height: 80px; }
  .cover-subtitle {
    position: absolute;
    left: 137px;
    top: 302px;
    width: 373px;
    height: 133px;
    border: 1px solid var(--rule);
    text-align: center;
    font-size: 26px;
    line-height: 36px;
  }
  .subtitle-text {
    position: absolute;
    left: 0;
    top: 2px;
    width: 100%;
  }
  .subtitle-count {
    font-size: 44px;
    line-height: 36px;
  }
  .cover-artwork {
    position: absolute;
    z-index: 1;
    left: 180px;
    top: 412px;
    width: 285px;
    height: 348px;
    border-radius: 46% 46% 40% 40%;
    background: linear-gradient(180deg, var(--gem-light) 0%, var(--gem-mid) 26%, var(--rock-mid) 44%, var(--rock-dark) 100%);
  }
  .cover-author {
    position: absolute;
    left: 0;
    top: 768px;
    width: 100%;
    padding-left: 34px;
    text-align: center;
    font-size: 42px;
    line-height: 50px;
    font-weight: 300;
  }
</style>
</head>
<body>
  <main class="canvas">
    <article class="book-cover">
      <div class="cover-spine"></div>
      <h1 class="cover-title">
        <span class="title-line title-lead">Founders</span>
        <span class="title-line title-join">behind the</span>
        <span class="title-line title-main-1">Quiet Trade</span>
        <span class="title-line title-main-2">Boom</span>
      </h1>
      <p class="cover-subtitle"><span class="subtitle-text"><span class="subtitle-count">25</span> stories of success<br>from discovering hidden<br>opportunities</span></p>
      <div class="cover-artwork" role="img" aria-label="A pale blue cut diamond emerging from the top of a dark, rough lump of coal"></div>
      <p class="cover-author">Dorian Pelham</p>
    </article>
  </main>
</body>
</html>
```